Cedar Lantern Steward Book Cover and Back Design

DESIGN BRIEF: The Cedar Lantern Steward Book Cover
Author: Mayor Calvin T. Ashby
Title: The Cedar Lantern Steward
Subtitle: Raising Stewards who shape neighborhoods
Genre: Leadership / Personal Development / Public Service
Format: Paperback + eBook + Hardcover
Design a visually compelling, iconic book cover that captures the essence of authentic, legacy-driven leadership using the metaphor of the mango tree. The cover should be vibrant, symbolic, and memorable—something that could stand alone as a brand and invite both credibility and curiosity.
Cover should NOT include:
Author’s face or personal photo
Overly busy visuals or political imagery
Literal images of mayors, buildings, or people
Cover SHOULD include:
A single iconic mango tree or mango fruit with visible deep roots
A vibrant and rich color palette—think mango orange, deep green, warm gold, and earth tones
A design that feels both modern and timeless, with symbolic depth
A sense of growth, depth, and legacy
Room for bold typography that pops in print and thumbnails
🖼️ VISUAL CONCEPT IDEAS
(Designer may interpret creatively, but these are preferred themes.)
A stylized mango tree with glowing mangoes and roots extending downward, set against a vibrant background (sunrise or rich green sky)
A mango fruit icon with leaves and roots subtly worked into the shape — could be used across brand platforms
Optional: Split background showing transformation — one side dry/cracked earth, the other lush and fruitful
Clean, modern layout with breathing space and balance between image and title
✍️ TYPOGRAPHY
Title Font: Strong, elegant serif or modern classic (e.g., Playfair Display, Garamond, or Libre Baskerville)
Subtitle Font: Clean and crisp sans serif (e.g., Lato, Montserrat)
Author Name: Bold, uppercase — not oversized, but clearly legible
🔠 COPY FOR COVER
Title:
The Cedar Lantern Steward
Subtitle:
Raising Stewards Who Shape Neighborhoods
Author Name:
Mayor Calvin T. Ashby
Optional Tagline or Teaser (for back or spine):
Stop performing like a politician. Start producing like a leader.
🔧 FORMAT DELIVERABLES
Front cover (paperback and hardcover versions)
Spine and back cover layout (with placeholder for barcode and description)
Web-optimized version for Veltrona SPX and other retailers
Square version for social media promotion
Optional: Icon version of tree or mango for branding
Back of book: Are you tired of leadership that looks impressive but produces no lasting fruit?
In a culture obsessed with image over integrity, quick wins over deep roots, and self-promotion over public service, we need a new kind of leader—one who leads for legacy, not likes.
What if you stopped leading like an apple tree—and started leading like a mango tree?
Apple trees grow fast and look good for a season, but their shallow roots can’t weather the storms. Mango trees grow slowly, but they last for generations—producing sweet, lasting fruit long after their planter is gone.
This isn’t just a metaphor. It’s a mindset shift. And it’s the key to leadership that actually transforms people, places, and policy.
Mayor Calvin Ashby has spent over a decade turning Dumfries, Virginia, from a town people drove through into a town people now drive to. Under his leadership:
• A former landfill became a half-billion-dollar resort
• A forgotten town rediscovered its purpose• A generation of young people began to see public service as purpose, not performance
In The Cedar Lantern Steward, you’ll discover how to:
✅ Lead from your authentic strengths—not trends or titles✅ Identify the unique problem you were born to solve✅ Build coalitions rooted in trust, not transaction✅ Make decisions that create sustainable change✅ Develop future leaders who multiply your impact✅ Leave a legacy that grows long after you’re gone
Whether you’re an elected official, aspiring public servant, nonprofit founder, or community-builder, this book will help you lead like a tree: planted deeply, growing steadily, and bearing fruit that feeds others for generations.
Stop performing like a politician. Start producing like a leader.Plant deep. Lead strong. Leave fruit that lasts.
By the time you finish this book, you won’t just understand the mango tree model—you’ll own it. You’ll walk away with clarity, courage, and a roadmap to become the kind of leader your community needs and your future demands.
Leadership

```html
<!DOCTYPE html>
<html lang="en">
<head>
<meta charset="utf-8">
<title>The Cedar Lantern Steward — Front Cover</title>
<link rel="stylesheet" href="https://fonts.googleapis.com/css2?family=Bebas+Neue&family=Montserrat:wght@500;600&display=swap">
<style>
  :root {
    --page-bg: #ffffff;
    --cover-orange: #b04208;
    --cover-brown: #5b3514;
    --cover-green: #133327;
    --cream: #f7d99a;
    --glow-gold: #f4c443;
    --glow-amber: #e08a1f;
    --leaf-green: #2f5a26;
    --root-earth: #4a2a12;
  }
  html, body {
    margin: 0;
    padding: 0;
    width: 1200px;
    height: 1200px;
    overflow: hidden;
    background: var(--page-bg);
  }
  .book-cover {
    position: absolute;
    left: 221px;
    top: 31px;
    width: 757px;
    height: 1137px;
    overflow: hidden;
    background: linear-gradient(90deg,
      var(--cover-orange) 0%,
      var(--cover-orange) 20%,
      var(--cover-brown) 38%,
      var(--cover-green) 56%,
      var(--cover-green) 100%);
  }
  .author-name {
    position: absolute;
    top: 50px;
    left: 0;
    width: 100%;
    margin: 0;
    text-align: center;
    font-family: "Montserrat", sans-serif;
    font-weight: 600;
    font-size: 34px;
    letter-spacing: 0.5px;
    color: var(--cream);
  }
  .tree-artwork {
    position: absolute;
    left: 175px;
    top: 116px;
    width: 412px;
    height: 600px;
    border-radius: 50% 50% 46% 46%;
    background:
      radial-gradient(ellipse 55% 40% at 50% 30%, var(--leaf-green) 0%, rgba(47,90,38,0.85) 60%, rgba(47,90,38,0) 100%),
      radial-gradient(ellipse 50% 38% at 50% 52%, var(--glow-gold) 0%, var(--glow-amber) 45%, rgba(224,138,31,0) 100%),
      radial-gradient(ellipse 45% 30% at 50% 82%, var(--root-earth) 0%, rgba(74,42,18,0.6) 55%, rgba(74,42,18,0) 100%);
    filter: blur(2px);
  }
  .cover-title {
    position: absolute;
    left: 0;
    top: 0;
    width: 757px;
    height: 1137px;
  }
  .cover-title text {
    font-family: "Bebas Neue", sans-serif;
    fill: var(--cream);
  }
  .subtitle {
    position: absolute;
    left: 0;
    top: 1058px;
    width: 100%;
    margin: 0;
    text-align: center;
    font-family: "Montserrat", sans-serif;
    font-weight: 500;
    font-size: 26px;
    letter-spacing: 0.3px;
    color: var(--cream);
  }
</style>
</head>
<body>
  <main class="book-cover">
    <p class="author-name">Mayor Calvin T. Ashby</p>

    <div class="tree-artwork" role="img"
         aria-label="Painted tree with glowing fruit, a large central fruit, and deep roots spreading into the earth against a golden sunrise"></div>

    <svg class="cover-title" viewBox="0 0 757 1137" aria-labelledby="book-title">
      <title id="book-title">The Cedar Lantern Steward</title>
      <text x="378.5" y="666" font-size="100" text-anchor="middle">THE</text>
      <text x="53" y="808" font-size="174" textLength="656" lengthAdjust="spacingAndGlyphs">CEDAR LANTERN</text>
      <text x="53" y="1032" font-size="291" textLength="656" lengthAdjust="spacingAndGlyphs">STEWARD</text>
    </svg>

    <p class="subtitle">Raising Stewards who shape neighborhoods</p>
  </main>
</body>
</html>
```